依頼詳細
【サイトの最大の要望】
①未経験の20代の求職者の登録者を増やす。
(短大卒・新卒・第二新卒・インターンシップの大学生)
②特に東京23区のエリアの強化

【強み】
・人材教育型採用支援
・未経験でも取れる
・アカデミー(代表自体が話す)

【ターゲット】
10代~20代の経理未経験者
(どちらかというと女性)
経理未経験の短大卒・新卒・第二新卒・インターンシップの大学生

【デザインについて】
・デザインテイストは「 モダン/ナチュラル/優しい/シンプル/清潔な/少し重厚感/ちょっと派手」

【参考サイト】
https://mofam.jp/
https://www.joblinvo.com/
https://senokuruto.jp/

【サイトマップ】
下記URL内のサイトマップを参照ください。
https://3.filebako.example/0722-b83d1e9a04fc2b67d51a0e4c88f7d2b1

■TOPページにGメニューとは別にデザインの入り口を必須で設けて頂きたいコン

テンツは以下となります。
(それ以外のページに関してはワークポッカーにお任せします)

サイトURL
http://tenuvel.com/
ページ数
1ページ
希望イメージ
シンプル 複雑
単色 カラフル
暗い 明るい
日常 高級
遊び心 厳粛
未来的 伝統的
女性的 男性的
希望する色
緑系、黄・オレンジ系、グレー系、黄・オレンジ系/グレー系/緑系(さし色)/ピンクベージュ
納品ファイル
• イラストレーター形式 (.ai)
• フォトショップ形式 (.psd)
• PNG形式 (.png)
補足説明
【店舗へのご連絡はおやめください】
ワークポッケ規約にもありますが、店舗への通常業務に支障が出るため、
直接電話等のお問い合わせをお控え頂きますよう、ご協力願います。

【素材写真】
下記よりダウンロードしてご使用ください。

また、ピクセモのカンプ画像をご使用ください。
選定後に正規データをお渡し致します。
(画像はマンスリーパック内でお願い致します。)
ワイヤーフレームを添付しますので、
参照ください。
先程の追記では説明不足でしてので、
補足致します。

サイトマップが確定する前に作成したワイヤーフレームになります。
決定版サイトマップを基に作成頂ければと思います。

ワイヤーフレームを添付することでデザインが全て同じになってしまう事を
避けたかったので、このタイミングで添付致しました。

ワイヤーフレームはあくまで参考として認識頂ければと思います。

宜しくお願い致します。

デザインの構成や色合いがとても素敵で訴求したいターゲットにも合っていると思いました。

選定させて頂きました。

引き続き、宜しくお願い致します。

```html
<!DOCTYPE html>
<html lang="ja">
<head>
<meta charset="utf-8">
<title>つむぎコラボ｜経理未経験者のための人材教育型採用支援</title>
<link rel="stylesheet" href="https://fonts.googleapis.com/css2?family=Noto+Sans+JP:wght@400;500;700;900&family=Noto+Serif+JP:wght@500;700&family=Cormorant+Garamond:ital,wght@0,500;1,500&display=swap">
<style>
:root{
  --pink:#d8707b;
  --pink-soft:#e8a3a8;
  --pink-beige:#f3e3dc;
  --orange:#f39a2b;
  --orange-soft:#f7c07a;
  --green:#7dba4c;
  --gray:#6b6b6b;
  --ink:#333;
  --white:#fff;
  --line:#e2d7d2;
}
*{box-sizing:border-box;margin:0;padding:0}
html,body{width:1200px;height:5272px;overflow:hidden}
body{font-family:"Noto Sans JP",sans-serif;color:var(--ink);background:var(--white);position:relative}
section,header,nav,footer{position:relative;width:1200px;overflow:hidden}
.photo{position:absolute}
.btn{display:inline-block;font-size:13px;color:var(--white);background:var(--pink);padding:10px 34px;border-radius:3px}
.btn--outline{background:rgba(255,255,255,.15);border:1px solid var(--white)}
.ghost-word{position:absolute;font-family:"Cormorant Garamond",serif;font-style:italic;color:rgba(243,154,43,.22);line-height:1}

/* hero */
.hero{height:500px}
.hero__bg{inset:0;background:linear-gradient(115deg,#8c6a5a 0%,#c9a99a 35%,#e6d2c6 60%,#f2e6dd 100%)}
.hero__figure{left:60px;top:0;width:380px;height:500px;background:radial-gradient(ellipse at 40% 40%,rgba(200,70,70,.55),rgba(140,90,80,0) 70%)}
.hero__catch{position:absolute;left:560px;top:60px;font-family:"Noto Serif JP",serif;font-size:46px;color:var(--pink);line-height:1.5;transform:rotate(-8deg);text-shadow:0 0 12px rgba(255,255,255,.8)}
.hero__contact{position:absolute;right:24px;top:18px;display:flex;flex-direction:column;gap:8px;align-items:flex-end}
.tel{display:flex;align-items:center;gap:8px;background:var(--white);border:2px solid var(--orange);padding:6px 14px;border-radius:4px}
.tel__num{font-size:22px;font-weight:900;color:var(--orange)}
.tel small{display:block;font-size:10px;color:var(--gray)}
.mail-btn{background:var(--orange);color:var(--white);font-size:13px;padding:8px 16px;border-radius:4px;display:flex;gap:6px;align-items:center}
.brand{position:absolute;left:130px;top:278px}
.brand__tag{font-size:13px;color:var(--white);margin-bottom:6px}
.brand__name{display:flex;align-items:center;gap:10px;font-size:30px;font-weight:700;color:var(--orange)}
.brand__mark{width:26px;height:26px;background:var(--orange)}
.hero__links{position:absolute;left:130px;top:370px;display:flex;gap:14px}
.hero__links a{background:var(--pink);color:var(--white);font-size:14px;padding:12px 24px;border-radius:3px;text-decoration:none}

/* nav */
.gnav{height:56px;background:var(--pink);display:flex;justify-content:center;align-items:center;gap:0}
.gnav a{color:var(--white);font-size:13px;text-decoration:none;padding:0 20px;border-right:1px solid rgba(255,255,255,.5)}
.gnav a:last-child{border:none}

/* strength */
.strength{height:200px;text-align:center;padding-top:36px}
.strength__title{font-size:30px;font-weight:700}
.strength__lead{font-size:13px;line-height:1.8;margin-top:12px;color:var(--gray)}
.strength__note{font-size:12px;color:var(--pink);margin-top:8px}
.strength svg{position:absolute;left:0;bottom:0}

/* college */
.college{height:194px;text-align:center;padding-top:40px}
.college .ghost-word{left:150px;top:20px;font-size:140px}
.college__title{position:relative;font-size:32px;font-weight:700;color:var(--orange)}
.college__sub{position:relative;font-size:16px;color:var(--pink);margin-top:6px}

/* grid */
.academy{height:1070px}
.academy__row{position:absolute;left:0;width:1200px}
.academy__row--1{top:0;height:400px}
.academy__row--2{top:400px;height:330px}
.academy__row--3{top:730px;height:340px}
.panel{position:absolute;color:var(--white);padding:40px 44px}
.panel h3{font-size:30px;font-weight:700;margin-bottom:18px}
.panel p{font-size:13px;line-height:1.9}
.panel .btn{margin-top:26px;background:transparent;border:1px solid var(--white)}
.panel--orange{left:0;top:0;width:600px;height:400px;background:rgba(232,140,50,.82)}
.panel--pink{left:0;top:0;width:560px;height:340px;background:rgba(214,112,118,.88)}
.dates{position:absolute;left:640px;top:40px;width:280px;height:250px;background:var(--white);padding:26px 30px;box-shadow:0 2px 10px rgba(0,0,0,.12)}
.dates h3{font-size:20px;font-weight:700;margin-bottom:14px}
.dates li{list-style:none;font-size:12px;line-height:1.8;color:var(--gray)}
.dates .btn{margin-top:14px;padding:7px 28px;font-size:12px}

/* voice */
.voice{height:940px;text-align:center}
.voice .ghost-word{left:460px;top:420px;font-size:130px;color:rgba(243,154,43,.2)}
.avatar{position:absolute;width:110px;height:110px;border-radius:50%;background:linear-gradient(135deg,#d9cfc9,#9e8f88)}
.voice__title{position:absolute;left:0;width:1200px;top:520px;font-size:22px;font-weight:700}
.voice__btn{position:absolute;left:540px;top:570px}
.voice__note{position:absolute;left:466px;top:640px;width:140px;background:var(--orange-soft);color:var(--white);font-size:11px;line-height:1.6;padding:10px}

/* steps */
.steps{height:660px}
.steps__bg{inset:0;background:linear-gradient(180deg,#c8c8c8,#e9e9e9 60%,#f4f0ec)}
.steps__title{position:absolute;left:0;width:1200px;top:90px;text-align:center;font-size:20px;font-weight:700}
.step-cards{position:absolute;left:170px;top:150px;display:flex;gap:22px}
.step{width:200px;height:230px;background:rgba(255,255,255,.92);text-align:center;padding-top:34px}
.step__num{font-family:"Noto Serif JP",serif;font-size:90px;color:#d23c3c;line-height:1}
.step__label{font-size:18px;font-weight:700;color:var(--pink);margin-top:24px}
.step-actions{position:absolute;left:170px;top:430px;display:flex;gap:160px}
.step-actions a{width:360px;height:96px;display:flex;align-items:center;justify-content:center;color:var(--white);font-size:18px;font-weight:700;text-decoration:none}
.cta--entry{background:var(--orange)}
.cta--dl{background:var(--green)}

/* jobs */
.jobs{height:620px;text-align:center;padding-top:70px}
.jobs h2{font-size:24px;font-weight:700}
.job-list{display:flex;justify-content:center;gap:16px;margin-top:30px;text-align:left}
.job{width:230px;height:330px;border:1px solid var(--line);padding:18px;font-size:12px;color:var(--gray);line-height:1.8}
.job__co{font-weight:700;color:var(--ink);font-size:13px}
.job dt{color:var(--ink);font-weight:700;margin-top:14px}
.job hr{border:none;border-top:1px solid var(--line);margin:10px 0}
.jobs .btn{margin-top:34px;background:var(--white);color:var(--ink);border:1px solid var(--gray)}

/* column */
.column{height:400px}
.column__lead{position:absolute;left:0;top:20px;width:300px;height:340px;background:var(--orange);color:var(--white);padding:40px 32px}
.column__lead h2{font-size:26px;font-weight:700;margin-bottom:16px}
.column__lead p{font-size:12px;line-height:1.8}
.column__lead .btn{margin-top:30px;background:transparent;border:1px solid var(--white)}
.column__list{position:absolute;left:330px;top:50px;display:flex;gap:16px}
.card{width:200px;font-size:11px;line-height:1.8;color:var(--gray)}
.card__thumb{height:110px;background:linear-gradient(135deg,#cfc5c0,#8f8580)}
.card h3{font-size:13px;color:var(--ink);margin:8px 0 4px}

/* contact */
.contact{height:360px}
.contact__bg{inset:0;background:linear-gradient(120deg,#e9e6e2,#f7f4f1 50%,#c9c2bd)}
.contact h2{position:absolute;left:0;width:1200px;top:70px;text-align:center;font-size:22px;font-weight:700}
.contact__row{position:absolute;left:170px;top:140px;display:flex;gap:60px}
.contact__tel{width:380px;height:110px;background:var(--white);border:3px solid var(--orange);display:flex;align-items:center;justify-content:center;gap:14px}
.contact__tel b{font-size:38px;font-weight:900;color:var(--orange)}
.contact__tel small{display:block;font-size:11px;color:var(--gray)}
.contact__mail{width:380px;height:110px;background:var(--orange);color:var(--white);font-size:26px;font-weight:700;display:flex;align-items:center;justify-content:center;gap:12px}

/* footer */
.site-footer{height:272px;background:var(--pink-beige)}
.footer__brand{position:absolute;left:60px;top:36px}
.footer__brand .brand__name{font-size:22px}
.footer__brand .brand__tag{color:var(--gray);font-size:11px}
.footer__addr{font-size:11px;color:var(--gray);line-height:1.8;margin-top:10px}
.footer__lead{position:absolute;left:420px;top:30px;font-size:12px;color:var(--pink)}
.footer__links{position:absolute;left:420px;top:60px;display:flex;gap:50px}
.footer__links ul{list-style:none;font-size:11px;line-height:2.1;color:var(--gray)}
.footer__links li::before{content:"› ";color:var(--pink)}
.footer__sub{position:absolute;right:40px;top:200px;font-size:11px;color:var(--gray)}
.copyright{position:absolute;left:0;bottom:0;width:1200px;height:32px;background:var(--pink);color:var(--white);font-size:11px;text-align:center;line-height:32px}
</style>
</head>
<body>

<header class="hero">
  <div class="photo hero__bg" role="img" aria-label="傘を持って空を見上げる女性の写真"></div>
  <div class="photo hero__figure" role="img" aria-label="赤い傘を広げる女性のシルエット"></div>
  <p class="hero__catch">経理の輝きを<br>あなたの手に</p>
  <div class="hero__contact">
    <div class="tel">
      <svg width="20" height="20" viewBox="0 0 24 24"><path fill="#f39a2b" d="M6.6 10.8a15 15 0 0 0 6.6 6.6l2.2-2.2a1 1 0 0 1 1-.25 11.4 11.4 0 0 0 3.6.6 1 1 0 0 1 1 1V20a1 1 0 0 1-1 1A17 17 0 0 1 3 4a1 1 0 0 1 1-1h3.5a1 1 0 0 1 1 1c0 1.25.2 2.45.6 3.6a1 1 0 0 1-.25 1z"/></svg>
      <div><span class="tel__num">0120-418-276</span><small>受付時間 平日10:00〜19:00</small></div>
    </div>
    <div class="mail-btn">
      <svg width="16" height="12" viewBox="0 0 16 12"><rect x="0.5" y="0.5" width="15" height="11" fill="none" stroke="#fff"/><path d="M1 1l7 6 7-6" fill="none" stroke="#fff"/></svg>
      お問い合わせ
    </div>
  </div>
  <div class="brand">
    <p class="brand__tag">東京・神奈川 経理未経験専門人材紹介・派遣</p>
    <p class="brand__name"><span class="brand__mark"></span>つむぎコラボ</p>
  </div>
  <nav class="hero__links">
    <a href="#">経理未経験者の方へ</a>
    <a href="#">求人一覧</a>
    <a href="#">企業の方へ</a>
  </nav>
</header>

<nav class="gnav">
  <a href="#">つむぎコラボについて</a>
  <a href="#">スタッフ紹介</a>
  <a href="#">つむぎカレッジ実施日</a>
  <a href="#">よくある質問</a>
  <a href="#">求人情報</a>
  <a href="#">卒業生の声</a>
  <a href="#">つむぎコラム</a>
  <a href="#">会社概要</a>
</nav>

<section class="strength">
  <h2 class="strength__title">つむぎコラボの強みは、人材教育型採用支援</h2>
  <p class="strength__lead">未経験の方でも安心して経理のお仕事に挑戦できるよう、基礎から丁寧にサポートします。<br>学びながら成長し、あなたに合った職場との出会いをお手伝いします。</p>
  <p class="strength__note">未経験者を育てるためのセミナーを開催中</p>
  <svg width="1200" height="40" viewBox="0 0 1200 40"><path d="M0 2H560L600 38L640 2H1200" fill="none" stroke="#d8707b" stroke-width="1.5"/></svg>
</section>

<section class="college">
  <span class="ghost-word">College</span>
  <h2 class="college__title">つむぎカレッジ</h2>
  <p class="college__sub">経理未経験者のための無料セミナー</p>
</section>

<section class="academy">
  <div class="academy__row academy__row--1">
    <div class="photo" style="left:0;top:0;width:600px;height:400px;background:linear-gradient(135deg,#b9a89c,#7f6e64)" role="img" aria-label="セミナーで講義を受ける受講生の写真"></div>
    <div class="photo" style="left:600px;top:0;width:600px;height:400px;background:linear-gradient(135deg,#cfc6bf,#8a7f79)" role="img" aria-label="ホワイトボードの前で話す講師の写真"></div>
    <div class="panel panel--orange">
      <h3>想い</h3>
      <p>経理の仕事に興味はあるけれど、経験がないから不安。そんな方の背中を押したいという想いから、このセミナーは生まれました。</p>
      <p style="margin-top:12px">一人ひとりの歩みに寄り添い、自信を持って働き始められるよう全力で支えます。</p>
      <span class="btn">Read More</span>
    </div>
  </div>
  <div class="academy__row academy__row--2">
    <div class="photo" style="left:0;top:0;width:760px;height:330px;background:linear-gradient(135deg,#a99c92,#e0d8d2)" role="img" aria-label="ホワイトボードの前で説明する女性講師の写真"></div>
    <div class="photo" style="left:760px;top:0;width:440px;height:330px;background:linear-gradient(135deg,#d9d1cb,#a79b93)" role="img" aria-label="講義を聞く受講生の写真"></div>
    <div class="dates" style="left:640px">
      <h3>つむぎカレッジ実施日</h3>
      <ul>
        <li>2019年5月XX日　開催</li>
        <li>2019年5月XX日　開催</li>
        <li>2019年6月XX日　開催</li>
        <li>2019年6月XX日　開催</li>
        <li>2019年7月XX日　開催</li>
      </ul>
      <span class="btn">Read More</span>
    </div>
  </div>
  <div class="academy__row academy__row--3">
    <div class="photo" style="left:0;top:0;width:600px;height:340px;background:linear-gradient(135deg,#b7aaa0,#857870)" role="img" aria-label="授業中の教室の写真"></div>
    <div class="photo" style="left:560px;top:0;width:640px;height:340px;background:linear-gradient(135deg,#e4ddd8,#9a8f88)" role="img" aria-label="笑顔で座るスーツ姿の女性の写真"></div>
    <div class="panel panel--pink">
      <h3>なぜ無料なのか</h3>
      <p>当社は企業様からの紹介手数料で運営しているため、求職者の方は費用をかけずに学ぶことができます。</p>
      <p style="margin-top:12px">学んだ知識を活かし、長く活躍していただくことが私たちの一番の願いです。</p>
      <span class="btn">Read More</span>
    </div>
  </div>
</section>

<section class="voice">
  <div class="avatar" style="left:230px;top:330px" role="img" aria-label="卒業生の顔写真"></div>
  <div class="avatar" style="left:320px;top:460px;width:90px;height:90px" role="img" aria-label="卒業生の顔写真"></div>
  <div class="avatar" style="left:130px;top:620px" role="img" aria-label="卒業生の顔写真"></div>
  <div class="avatar" style="left:60px;top:440px;width:90px;height:90px" role="img" aria-label="卒業生の顔写真"></div>
  <div class="avatar" style="left:250px;top:760px;width:90px;height:90px" role="img" aria-label="卒業生の顔写真"></div>
  <div class="avatar" style="left:460px;top:330px;width:90px;height:90px" role="img" aria-label="卒業生の顔写真"></div>
  <div class="avatar" style="left:600px;top:320px" role="img" aria-label="卒業生の顔写真"></div>
  <div class="avatar" style="left:800px;top:330px;width:90px;height:90px" role="img" aria-label="卒業生の顔写真"></div>
  <div class="avatar" style="left:880px;top:460px" role="img" aria-label="卒業生の顔写真"></div>
  <div class="avatar" style="left:1060px;top:400px;width:90px;height:90px" role="img" aria-label="卒業生の顔写真"></div>
  <div class="avatar" style="left:1040px;top:620px" role="img" aria-label="卒業生の顔写真"></div>
  <div class="avatar" style="left:840px;top:720px;width:90px;height:90px" role="img" aria-label="卒業生の顔写真"></div>
  <div class="avatar" style="left:650px;top:740px;width:100px;height:100px" role="img" aria-label="卒業生の顔写真"></div>
  <span class="ghost-word">Voice</span>
  <h2 class="voice__title">卒業生の声</h2>
  <span class="btn voice__btn">Read More</span>
  <p class="voice__note">アイコンホバーで<br>コメントが表示されます</p>
</section>

<section class="steps">
  <div class="photo steps__bg" role="img" aria-label="オフィスで働く人々のモノクロ写真"></div>
  <h2 class="steps__title">就職までのステップ</h2>
  <div class="step-cards">
    <div class="step"><div class="step__num">1</div><p class="step__label">エントリー</p></div>
    <div class="step"><div class="step__num">2</div><p class="step__label">テキスト</p></div>
    <div class="step"><div class="step__num">3</div><p class="step__label">テキスト</p></div>
    <div class="step"><div class="step__num">4</div><p class="step__label">就職</p></div>
  </div>
  <div class="step-actions">
    <a href="#" class="cta--entry">つむぎカレッジへのエントリー</a>
    <a href="#" class="cta--dl">資料ダウンロード</a>
  </div>
</section>

<section class="jobs">
  <h2>求人情報</h2>
  <div class="job-list">
    <dl class="job"><p class="job__co">株式会社　未経験OK</p><p>正社員</p><hr><dt>■仕事内容</dt><dd>経理補助・伝票入力・請求書作成など</dd><dt>■給与</dt><dd>230,000〜300,000</dd><dt>■勤務地</dt><dd>東京都23区内</dd></dl>
    <dl class="job"><p class="job__co">株式会社　未経験OK</p><p>正社員</p><hr><dt>■仕事内容</dt><dd>経理補助・伝票入力・請求書作成など</dd><dt>■給与</dt><dd>230,000〜300,000</dd><dt>■勤務地</dt><dd>東京都23区内</dd></dl>
    <dl class="job"><p class="job__co">株式会社　未経験OK</p><p>正社員</p><hr><dt>■仕事内容</dt><dd>経理補助・伝票入力・請求書作成など</dd><dt>■給与</dt><dd>230,000〜300,000</dd><dt>■勤務地</dt><dd>東京都23区内</dd></dl>
    <dl class="job"><p class="job__co">株式会社　未経験OK</p><p>正社員</p><hr><dt>■仕事内容</dt><dd>経理補助・伝票入力・請求書作成など</dd><dt>■給与</dt><dd>230,000〜300,000</dd><dt>■勤務地</dt><dd>東京都23区内</dd></dl>
  </div>
  <span class="btn">Read More</span>
</section>

<section class="column">
  <div class="column__lead">
    <h2>つむぎコラム</h2>
    <p>経理の基礎知識や、働き方のヒントをお届けします。未経験からのキャリアづくりにお役立てください。</p>
    <span class="btn">Read More</span>
  </div>
  <div class="column__list">
    <article class="card"><div class="card__thumb" role="img" aria-label="書類を手にする人の写真"></div><h3>コラムタイトル</h3><p>コラムの導入文が入ります。コラムの導入文が入ります。</p></article>
    <article class="card"><div class="card__thumb" role="img" aria-label="ノートパソコンで作業する人の写真"></div><h3>コラムタイトル</h3><p>コラムの導入文が入ります。コラムの導入文が入ります。</p></article>
    <article class="card"><div class="card__thumb" role="img" aria-label="電卓と帳簿の写真"></div><h3>コラムタイトル</h3><p>コラムの導入文が入ります。コラムの導入文が入ります。</p></article>
    <article class="card"><div class="card__thumb" role="img" aria-label="オフィスで打ち合わせする人の写真"></div><h3>コラムタイトル</h3><p>コラムの導入文が入ります。コラムの導入文が入ります。</p></article>
  </div>
</section>

<section class="contact">
  <div class="photo contact__bg" role="img" aria-label="デスクでパソコンに向かう手元の写真"></div>
  <h2>お問い合わせ（総合）</h2>
  <div class="contact__row">
    <div class="contact__tel">
      <svg width="40" height="40" viewBox="0 0 24 24"><path fill="#f39a2b" d="M6.6 10.8a15 15 0 0 0 6.6 6.6l2.2-2.2a1 1 0 0 1 1-.25 11.4 11.4 0 0 0 3.6.6 1 1 0 0 1 1 1V20a1 1 0 0 1-1 1A17 17 0 0 1 3 4a1 1 0 0 1 1-1h3.5a1 1 0 0 1 1 1c0 1.25.2 2.45.6 3.6a1 1 0 0 1-.25 1z"/></svg>
      <div><b>0120-418-276</b><small>受付時間 平日10:00〜19:00</small></div>
    </div>
    <div class="contact__mail">
      <svg width="34" height="24" viewBox="0 0 16 12"><rect x="0.5" y="0.5" width="15" height="11" fill="none" stroke="#fff"/><path d="M1 1l7 6 7-6" fill="none" stroke="#fff"/></svg>
      メールでお問い合わせ
    </div>
  </div>
</section>

<footer class="site-footer">
  <div class="footer__brand">
    <p class="brand__tag">東京・神奈川 経理未経験専門人材紹介・派遣</p>
    <p class="brand__name"><span class="brand__mark" style="width:20px;height:20px"></span>つむぎコラボ</p>
    <p class="footer__addr">〒100-0000<br>東京都千代田区架空町1-2-3<br>つむぎビル5階<br>TEL 0120-418-276</p>
  </div>
  <p class="footer__lead">東京・神奈川の経理未経験専門人材紹介・派遣ならつむぎコラボへ</p>
  <div class="footer__links">
    <ul><li>つむぎコラボについて</li><li>スタッフ紹介</li><li>つむぎカレッジ実施日</li><li>よくある質問</li></ul>
    <ul><li>経理未経験者の方へ</li><li>つむぎカレッジ</li><li>卒業生の声</li><li>求人情報</li></ul>
    <ul><li>よくある質問</li><li>会社概要</li><li>つむぎコラム</li><li>お問い合わせ</li></ul>
  </div>
  <p class="footer__sub">› 個人情報保護方針　› サイトマップ</p>
  <p class="copyright">COPYRIGHT © 株式会社つむぎコラボ All rights reserved.</p>
</footer>

</body>
</html>
```